Webdesign für einen gemeinnützigen Verein
Zielgruppe
Merovalien e. V. ist ein gemeinnütziger Verein der sich auf die Fahne geschrieben hat sich für Inklusive und Vielfalt einzusetzen. Wir unterstützen Menschen mit Behinderung beim selbstbestimmten Leben und helfen auch bei Anträgen etc. Des weiteren helfen wir Firmen, Vereinen und stonstigen Organisationen Ihre Inhalte und Auftritte barrierefrei zu gestallten. Wir Testen Apps und Websites und geben hier Feedback.
Aufgabenstellung
Wir möchten ein WordPress Theme das responsiv und persistent ist. Wir möchten die Inhalte später mit WordPress Einpflege und die Seite managen.
Unser Corporate Design steht bereits und beinhaltet die Pride Farben und sollte somit in einem hellen und dunklen Design umgesetzt werden. Wir möchten hier 2 Varianten vom Homepage Design (Darkmode)
Poppins ist unsere Schriftart für Textinhalte
Google Fonds möchten wir nicht nutzen
Passende Social Media Icons

```html
<!DOCTYPE html>
<html lang="de">
<head>
<meta charset="utf-8">
<title>Merovalien e. V. – Verein</title>
<link rel="stylesheet" href="https://fonts.googleapis.com/css2?family=Poppins:wght@300;400;500;600;700&display=swap">
<style>
:root{
  --bg-top:#1b1840;
  --bg-bottom:#4b1572;
  --ink:#1c1f3f;
  --text:#3a3a48;
  --accent:#5a1e86;
  --panel-grey:#e7e7e9;
  --white:#ffffff;
  --footer:#151a3b;
  --footer-text:#d8d9e6;
  --link:#2a8fd6;
  --rainbow:linear-gradient(90deg,#e53935,#fb8c00,#fdd835,#43a047,#1e88e5,#6a3fc8,#8e24aa);
}
*{box-sizing:border-box;margin:0;padding:0}
html,body{width:1200px;height:2434px;overflow:hidden}
body{
  position:relative;
  font-family:"Poppins",sans-serif;
  background:linear-gradient(180deg,var(--bg-top) 0%,#2b1a55 50%,var(--bg-bottom) 100%);
  color:var(--text);
}
.panel{position:absolute;overflow:hidden}
.mobile{left:42px;width:259px}
.desktop{left:338px;width:820px}

.loader{background:var(--white);top:43px;height:461px;display:flex;flex-direction:column;align-items:center;justify-content:flex-start}
.loader .mark{margin-top:210px;display:flex;align-items:center;gap:6px;font-weight:600;font-size:13px;color:var(--accent);letter-spacing:.5px}
.loader .mark i{width:22px;height:22px;border-radius:50%;background:var(--accent);display:block}
.loader .bar{margin-top:28px;width:142px;height:4px;border-radius:2px;background:var(--rainbow)}

.site-header{height:59px;background:var(--panel-grey);display:flex;align-items:center;position:relative}
.brand{display:flex;align-items:center;gap:7px;font-weight:500;color:var(--ink);font-size:14px;letter-spacing:.2px}
.brand i{width:22px;height:22px;border-radius:50%;background:var(--accent);display:block}
.desktop .site-header .brand{position:absolute;left:49px}
.nav{position:absolute;left:302px;display:flex;font-size:10.5px;color:var(--ink)}
.nav a{color:inherit;text-decoration:none;padding:1px 5px;margin-right:10px;border-radius:4px}
.nav a.active{background:var(--rainbow);color:var(--white)}
.toggle{position:absolute;left:728px;width:42px;height:22px;border-radius:11px;background:var(--white);display:flex;align-items:center;padding:0 3px;gap:6px}
.toggle .sun{width:16px;height:16px;border-radius:50%;background:var(--accent);position:relative}
.toggle .sun::after{content:"";position:absolute;left:5px;top:5px;width:6px;height:6px;border-radius:50%;background:var(--white)}
.mobile .site-header .brand{position:absolute;left:16px;font-size:10.5px;gap:5px}
.mobile .site-header .brand i{width:18px;height:18px}
.burger{position:absolute;right:18px;width:20px;height:20px;border-radius:6px;background:var(--rainbow);display:flex;flex-direction:column;justify-content:center;align-items:center;gap:2px}
.burger span{width:11px;height:2px;background:var(--white);border-radius:1px}

.hero{top:504px;height:461px;background:var(--white)}
.hero-visual{position:absolute;background:linear-gradient(180deg,#eeeeec 0%,#e2ded8 55%,#cfc7bd 100%)}
.desktop .hero-visual{left:49px;top:60px;width:720px;height:400px}
.mobile .hero-visual{left:0;top:59px;width:259px;height:402px}
.cta{position:absolute;transform:translateX(-50%);background:var(--accent);color:var(--white);font-size:8px;font-weight:600;letter-spacing:.3px;padding:7px 8px;border-radius:12px;white-space:nowrap}
.chev{position:absolute;transform:translateX(-50%);width:14px;height:8px}

.section-about{top:965px;height:460px}
.desktop.section-about{background:var(--panel-grey)}
.mobile.section-about,.mobile.section-why{background:var(--white)}
.section-why{top:1425px;height:461px}
.desktop.section-why{background:var(--white)}
h2{font-weight:600;color:var(--ink);text-align:center;letter-spacing:.2px}
.desktop h2{font-size:21px}
.mobile h2{font-size:14px;line-height:19px}
.photo{position:absolute;border-radius:8px}
.photo-hands{background:linear-gradient(160deg,#7fa0b8 0%,#d8c0ad 45%,#b88a70 100%)}
.photo-group{background:linear-gradient(160deg,#c9d3dc 0%,#8f9fb0 40%,#d8a34a 75%,#6d6f86 100%)}
.copy{position:absolute;text-align:justify}
.copy p{margin-bottom:13px}
.copy em{font-style:normal;color:var(--accent);font-weight:500}
.copy .closing{color:var(--accent);font-weight:500}
.desktop .copy{font-size:10.8px;line-height:15px}
.mobile .copy{font-size:6.6px;line-height:11.2px;left:17px;width:225px}
.mobile .copy p{margin-bottom:9px}
.to-top{position:absolute;width:22px;height:22px;border-radius:50%;background:var(--accent);display:flex;align-items:center;justify-content:center}

.footer{top:1886px;background:linear-gradient(180deg,#3d1766 0%,var(--footer) 22%);color:var(--footer-text);font-size:9.8px}
.desktop.footer{height:229px}
.mobile.footer{height:460px}
.f-brand{position:absolute;font-weight:500;font-size:17px;letter-spacing:1px;color:var(--white);display:flex;align-items:center;gap:6px}
.f-brand i{width:20px;height:20px;border-radius:50%;background:var(--white);display:block}
.tagline{position:absolute;text-align:center;font-size:8px;line-height:10px;color:var(--white);white-space:nowrap}
.tagline b{font-weight:500;font-size:9.5px;letter-spacing:.6px}
.f-list{position:absolute;list-style:none;line-height:18px;white-space:nowrap}
.addr span{display:inline-block;width:38px}
.email-field{width:142px;height:15px;border-radius:3px;background:#b4b6c4;color:#f2f2f6;font-size:9px;padding-left:7px;line-height:15px;margin-bottom:4px}
.newsletter{color:var(--link)}
.copyright{position:absolute;left:0;right:0;bottom:0;height:22px;background:var(--rainbow);color:var(--white);font-size:8.5px;text-align:center;line-height:22px}
.copyright b{font-weight:600}
</style>
</head>
<body>

<section class="panel mobile loader" aria-label="Ladebildschirm mobil">
  <div class="mark"><i></i>MEROVALIEN</div>
  <div class="bar"></div>
</section>
<section class="panel desktop loader" aria-label="Ladebildschirm Desktop">
  <div class="mark"><i></i>MEROVALIEN</div>
  <div class="bar"></div>
</section>

<section class="panel mobile hero">
  <header class="site-header">
    <div class="brand"><i></i>MEROVALIEN</div>
    <div class="burger"><span></span><span></span><span></span></div>
  </header>
  <div class="hero-visual" role="img" aria-label="Foto: Frauen sitzen vor einer weißen Wand und halten bunte Sprechblasen hoch"></div>
  <div class="cta" style="left:128px;top:346px">AUSFÜHRLICHE INFOS</div>
  <svg class="chev" style="left:128px;top:374px" viewBox="0 0 14 8"><path d="M1 1l6 6 6-6" fill="none" stroke="#fff" stroke-width="1.4"/></svg>
</section>

<section class="panel desktop hero">
  <header class="site-header">
    <div class="brand"><i></i>MEROVALIEN</div>
    <nav class="nav"><a>Home</a><a class="active">Verein</a><a>Projekte</a><a>Team</a><a>Blog</a><a>Wir im Netz</a><a>Kontakt</a></nav>
    <div class="toggle"><span class="sun"></span><svg width="9" height="9" viewBox="0 0 10 10"><path d="M7 1a4.5 4.5 0 1 0 2 7A4 4 0 0 1 7 1z" fill="#1c1f3f"/></svg></div>
  </header>
  <div class="hero-visual" role="img" aria-label="Foto: vier Frauen, eine davon im Rollstuhl, halten bunte Sprechblasen hoch"></div>
  <div class="cta" style="left:408px;top:342px">AUSFÜHRLICHE INFOS</div>
  <svg class="chev" style="left:408px;top:370px" viewBox="0 0 14 8"><path d="M1 1l6 6 6-6" fill="none" stroke="#fff" stroke-width="1.4"/></svg>
</section>

<section class="panel mobile section-about">
  <h2 style="margin-top:20px">WAS MACHT UNS AUS?</h2>
  <div class="photo photo-hands" style="left:81px;top:40px;width:97px;height:57px" role="img" aria-label="Foto: übereinandergelegte Hände"></div>
  <div class="copy" style="top:104px">
    <p><em>Alles begann vor einigen Jahren</em>, als eine Gruppe von Menschen mit unterschiedlichsten Hintergründen und Erfahrungen sich zusammenschloss, um gemeinsam für die Rechte von Menschen mit Behinderungen einzutreten. Wir merkten schnell, dass es in unserer Gesellschaft noch immer viele Barrieren gibt, die das selbstbestimmte Leben von Menschen mit Behinderungen erschweren.</p>
    <p>Doch wir waren nicht bereit, uns damit abzufinden und beschlossen, aktiv zu werden. Wir begannen uns zu vernetzen, tauschten uns über unsere Erfahrungen aus und arbeiteten gemeinsam an Lösungen. So entstand die Idee, eine Organisation zu gründen, die sich für die Förderung von Kommunikation und Inklusion von Menschen mit Behinderungen einsetzt – und so wurde Merovalien geboren.</p>
    <p>In den Anfangsjahren war es oft schwierig, Unterstützung zu finden und unsere Ziele in die Tat umzusetzen. Doch wir ließen uns nicht entmutigen und arbeiteten hart daran, unsere Vision von einer inklusiven Gesellschaft zu verwirklichen. Heute sind wir stolz darauf, dass unser Verein bereits vielen Menschen mit Behinderungen helfen konnte und dass wir in der Gesellschaft immer mehr Gehör finden.</p>
    <p class="closing">Wir sind dankbar für jeden, der sich uns anschließt und uns dabei unterstützt, Barrieren abzubauen und Menschen mit Behinderungen eine Stimme zu geben.</p>
  </div>
</section>

<section class="panel desktop section-about">
  <header class="site-header">
    <div class="brand"><i></i>MEROVALIEN</div>
    <nav class="nav"><a>Home</a><a class="active">Verein</a><a>Projekte</a><a>Team</a><a>Blog</a><a>Wir im Netz</a><a>Kontakt</a></nav>
    <div class="toggle"><span class="sun"></span><svg width="9" height="9" viewBox="0 0 10 10"><path d="M7 1a4.5 4.5 0 1 0 2 7A4 4 0 0 1 7 1z" fill="#1c1f3f"/></svg></div>
  </header>
  <h2 style="margin-top:22px">WIE ALLES BEGANN?</h2>
  <div class="photo photo-hands" style="left:111px;top:128px;width:142px;height:292px" role="img" aria-label="Foto: viele Hände übereinander als Zeichen des Zusammenhalts"></div>
  <div class="copy" style="left:277px;top:126px;width:450px">
    <p><em>Alles begann vor einigen Jahren</em>, als eine Gruppe von Menschen mit unterschiedlichsten Hintergründen und Erfahrungen sich zusammenschloss, um gemeinsam für die Rechte von Menschen mit Behinderungen einzutreten. Wir merkten schnell, dass es in unserer Gesellschaft noch immer viele Barrieren gibt, die das selbstbestimmte Leben von Menschen mit Behinderungen erschweren.</p>
    <p>Doch wir waren nicht bereit, uns damit abzufinden und beschlossen, aktiv zu werden. Wir begannen uns zu vernetzen, tauschten uns über unsere Erfahrungen aus und arbeiteten gemeinsam an Lösungen. So entstand die Idee, eine Organisation zu gründen, die sich für die Förderung von Kommunikation und Inklusion von Menschen mit Behinderungen einsetzt – und so wurde Merovalien geboren.</p>
    <p>In den Anfangsjahren war es oft schwierig, Unterstützung zu finden und unsere Ziele in die Tat umzusetzen. Doch wir ließen uns nicht entmutigen und arbeiteten hart daran, unsere Vision von einer inklusiven Gesellschaft zu verwirklichen. Heute sind wir stolz darauf, dass unser Verein bereits vielen Menschen mit Behinderungen helfen konnte und dass wir in der Gesellschaft immer mehr Gehör finden.</p>
    <p class="closing">Wir sind dankbar für jeden, der sich uns anschließt und uns dabei unterstützt, Barrieren abzubauen und Menschen mit Behinderungen eine Stimme zu geben.</p>
  </div>
  <div class="to-top" style="left:727px;top:420px"><svg width="12" height="12" viewBox="0 0 12 12"><path d="M6 11V1M1.5 5.5L6 1l4.5 4.5" fill="none" stroke="#fff" stroke-width="1.4"/></svg></div>
</section>

<section class="panel mobile section-why">
  <h2 style="margin-top:15px">WARUM HABEN<br>WIR DEN VEREIN GEGRÜNDET?</h2>
  <div class="photo photo-group" style="left:64px;top:55px;width:132px;height:148px" role="img" aria-label="Foto: Gruppe junger Menschen, einer im Rollstuhl"></div>
  <div class="copy" style="top:211px">
    <p><em>Wir haben Merovalien gegründet</em>, weil uns die Bedürfnisse von Menschen mit Behinderungen am Herzen liegen und wir uns für ihre Rechte und eine inklusive Gesellschaft einsetzen wollen. Wir haben selbst erlebt, wie schwer es sein kann, Barrieren zu überwinden und sich Gehör zu verschaffen. Deshalb wollten wir eine Organisation schaffen, die sich für mehr Barrierefreiheit bei digitalen Medien, eine bessere zwischenmenschliche Kommunikation und die Förderung von Selbstbestimmung und Empowerment von Menschen mit Behinderungen einsetzt.</p>
    <p>Unser Ziel ist es, eine Gesellschaft zu schaffen, in der jeder Mensch unabhängig von einer Behinderung vollständig integriert ist und selbstbestimmt leben kann. Wir glauben, dass jeder Einzelne dazu beitragen kann und dass jede Stimme zählt. Wir möchten Menschen ermutigen, sich für die Rechte von Menschen mit Behinderungen einzusetzen und Barrieren abzubauen. Wir sind stolz darauf, Teil dieser Bewegung zu sein und hoffen, dass auch du dich uns anschließt!</p>
  </div>
</section>

<section class="panel desktop section-why">
  <header class="site-header">
    <div class="brand"><i></i>MEROVALIEN</div>
    <nav class="nav"><a>Home</a><a class="active">Verein</a><a>Projekte</a><a>Team</a><a>Blog</a><a>Wir im Netz</a><a>Kontakt</a></nav>
    <div class="toggle"><span class="sun"></span><svg width="9" height="9" viewBox="0 0 10 10"><path d="M7 1a4.5 4.5 0 1 0 2 7A4 4 0 0 1 7 1z" fill="#1c1f3f"/></svg></div>
  </header>
  <h2 style="margin-top:22px">WARUM HABEN WIR DEN VEREIN GEGRÜNDET?</h2>
  <div class="copy" style="left:111px;top:144px;width:370px">
    <p><em>Wir haben Merovalien gegründet</em>, weil uns die Bedürfnisse von Menschen mit Behinderungen am Herzen liegen und wir uns für ihre Rechte und eine inklusive Gesellschaft einsetzen wollen. Wir haben selbst erlebt, wie schwer es sein kann, Barrieren zu überwinden und sich Gehör zu verschaffen. Deshalb wollten wir eine Organisation schaffen, die sich für mehr Barrierefreiheit bei digitalen Medien, eine bessere zwischenmenschliche Kommunikation und die Förderung von Selbstbestimmung und Empowerment von Menschen mit Behinderungen einsetzt.</p>
    <p>Unser Ziel ist es, eine Gesellschaft zu schaffen, in der jeder Mensch unabhängig von einer Behinderung vollständig integriert ist und selbstbestimmt leben kann. Wir glauben, dass jeder Einzelne dazu beitragen kann und dass jede Stimme zählt. Wir möchten Menschen ermutigen, sich für die Rechte von Menschen mit Behinderungen einzusetzen und Barrieren abzubauen. Wir sind stolz darauf, Teil dieser Bewegung zu sein und hoffen, dass auch du dich uns anschließt!</p>
  </div>
  <div class="photo photo-group" style="left:505px;top:144px;width:222px;height:248px" role="img" aria-label="Foto: lächelnde Gruppe junger Menschen, ein Mann im Rollstuhl"></div>
</section>

<footer class="panel mobile footer">
  <div class="f-brand" style="left:47px;top:38px"><i></i>MEROVALIEN</div>
  <div class="tagline" style="left:64px;top:62px;width:180px">— Verein für Vielfalt und Teilhabe —<br><b>Gemeinsam ohne Barrieren</b><br>für ein selbstbestimmtes Leben</div>
  <ul class="f-list addr" style="left:47px;top:111px">
    <li>Merovalien e. V.</li>
    <li>c/o Lindenhof Amselweg 14</li>
    <li>10999 Berlin</li>
    <li><span>Tel.</span>: +49 (0) 3000 5500 120</li>
    <li><span>Fax.</span>: +49 (0) 3000 5500 121</li>
    <li><span>E-Mail</span>: info@merovalien.de</li>
    <li>Service</li><li>Blog</li><li>Privacy &amp; Policy</li><li>Sitemap</li><li>Barrierefreiheit</li>
  </ul>
  <div style="position:absolute;left:47px;top:320px;width:200px">
    <div class="email-field">email</div>
    <ul class="f-list"><li class="newsletter">Abonnieren Sie unseren Newsletter!</li><li>Impressum</li><li>Datenschutzerklärung</li><li>Cookie-Richtlinie</li></ul>
  </div>
  <div class="copyright">© 2023, <b>MEROVALIEN</b> All rights reserved</div>
</footer>

<footer class="panel desktop footer">
  <div class="f-brand" style="left:49px;top:42px"><i></i>MEROVALIEN</div>
  <ul class="f-list addr" style="left:49px;top:76px">
    <li>Merovalien e. V.</li>
    <li>c/o Lindenhof Amselweg 14</li>
    <li>10999 Berlin</li>
    <li><span>Tel.</span>: +49 (0) 3000 5500 120</li>
    <li><span>Fax.</span>: +49 (0) 3000 5500 121</li>
    <li><span>E-Mail</span>: info@merovalien.de</li>
  </ul>
  <ul class="f-list" style="left:356px;top:94px">
    <li>Service</li><li>Blog</li><li>Privacy &amp; Policy</li><li>Sitemap</li><li>Barrierefreiheit</li>
  </ul>
  <div class="tagline" style="left:585px;top:24px;width:185px">— Verein für Vielfalt und Teilhabe —<br><b>Gemeinsam ohne Barrieren</b><br>für ein selbstbestimmtes Leben</div>
  <div style="position:absolute;left:585px;top:91px;width:200px">
    <div class="email-field">email</div>
    <ul class="f-list"><li class="newsletter">Abonnieren Sie unseren Newsletter!</li><li>Impressum</li><li>Datenschutzerklärung</li><li>Cookie-Richtlinie</li></ul>
  </div>
  <div class="to-top" style="left:727px;top:171px"><svg width="12" height="12" viewBox="0 0 12 12"><path d="M6 11V1M1.5 5.5L6 1l4.5 4.5" fill="none" stroke="#fff" stroke-width="1.4"/></svg></div>
  <div class="copyright">© 2023, <b>MEROVALIEN</b> All rights reserved</div>
</footer>

</body>
</html>
```